Land Buying Company Needs Letterhead for Direct Mail Marketing to Land Owners

We are looking for a professional letterhead that we will be including in our direct mail marketing. We will be sending this to land owners who may be interested in selling or purchasing land.

The letterhead needs to be editable. Headers and footers would look nice, but we are open. We would want it to include our address, website, phone, and email info. For right now the address to use for design purposes would the following:

Address: 415 Bramwell Avenue #600
Dallas, TX 75219
Website - www.quillridgeacres.example
Email - info@quillridgeacres.example
Phone - 866-402-ACRE

I have attached our logo zip file that we just had done on Pixel Guild. Let me know what questions you have, and thank you.

```html
<!DOCTYPE html>
<html lang="en">
<head>
<meta charset="utf-8">
<title>Quill Ridge Acres — Letterhead</title>
<link href="https://fonts.googleapis.com/css2?family=Open+Sans:wght@400;700&display=swap" rel="stylesheet">
<style>
  :root {
    --backdrop: #dfe9d6;
    --paper: #ffffff;
    --forest: #3f5a1c;
    --forest-deep: #2f4512;
    --leaf: #8cc63f;
    --ink: #4a4a4a;
    --rule: #b9b9b9;
    --watermark: #f2f2f2;
  }
  * { box-sizing: border-box; margin: 0; padding: 0; }
  html, body { width: 1200px; height: 784px; overflow: hidden; }
  body {
    background: var(--backdrop);
    display: flex; align-items: center; justify-content: center;
    font-family: "Open Sans", sans-serif;
  }
  .letterhead {
    position: relative;
    width: 528px; height: 744px;
    background: var(--paper);
    box-shadow: 0 6px 18px rgba(60, 80, 40, 0.18);
    overflow: hidden;
  }
  .corner { position: absolute; width: 150px; height: 80px; }
  .corner--top-right { top: 0; right: 0; }
  .corner--bottom-left { bottom: 0; left: 0; transform: rotate(180deg); }

  .brand {
    position: absolute; top: 44px; right: 168px;
    display: flex; align-items: center; gap: 10px;
    white-space: nowrap;
  }
  .brand__dot { width: 30px; height: 30px; border-radius: 50%; background: var(--forest); flex: none; }
  .brand__name {
    font-family: "Open Sans", sans-serif; font-weight: 700;
    font-size: 19px; letter-spacing: 1px; color: var(--leaf);
    text-transform: uppercase;
  }

  .watermark {
    position: absolute; left: 50%; top: 46%;
    width: 230px; height: 230px; margin: -115px 0 0 -115px;
    border-radius: 50%; background: var(--watermark);
  }

  .footer {
    position: absolute; left: 150px; right: 40px; bottom: 36px;
    text-align: center; color: var(--ink);
  }
  .footer__icons {
    display: flex; align-items: center; justify-content: center; gap: 8px;
    margin-bottom: 8px;
  }
  .footer__rule { width: 60px; height: 1px; background: var(--rule); }
  .footer__icon {
    width: 13px; height: 13px; border-radius: 50%; background: var(--forest);
    display: flex; align-items: center; justify-content: center;
  }
  .footer__address {
    font-weight: 700; font-size: 10px; color: var(--forest-deep);
    margin-bottom: 6px;
  }
  .footer__contacts { font-size: 9px; display: flex; justify-content: center; align-items: center; gap: 8px; white-space: nowrap; }
  .footer__sep { width: 1px; height: 11px; background: var(--leaf); }
</style>
</head>
<body>
  <main class="letterhead">
    <svg class="corner corner--top-right" viewBox="0 0 150 80" aria-hidden="true">
      <defs>
        <linearGradient id="leafFacet" x1="0" y1="0" x2="1" y2="1">
          <stop offset="0" stop-color="#e3f3c6"/>
          <stop offset="1" stop-color="#8cc63f"/>
        </linearGradient>
      </defs>
      <polygon points="0,0 150,0 150,80" fill="var(--forest)"/>
      <polygon points="80,0 150,0 150,36" fill="var(--forest-deep)"/>
      <polygon points="150,80 150,44 118,80" fill="url(#leafFacet)"/>
    </svg>
    <svg class="corner corner--bottom-left" viewBox="0 0 150 80" aria-hidden="true">
      <polygon points="0,0 150,0 150,80" fill="var(--forest)"/>
      <polygon points="80,0 150,0 150,36" fill="var(--forest-deep)"/>
      <polygon points="150,80 150,44 118,80" fill="url(#leafFacet)"/>
    </svg>

    <header class="brand">
      <span class="brand__dot"></span>
      <span class="brand__name">Quill Ridge Acres</span>
    </header>

    <div class="watermark" role="img" aria-label="Faint brand emblem watermark"></div>

    <footer class="footer">
      <div class="footer__icons">
        <span class="footer__rule"></span>
        <span class="footer__icon"><svg width="7" height="7" viewBox="0 0 10 10"><path d="M5 0a3.5 3.5 0 0 1 3.5 3.5C8.5 6 5 10 5 10S1.5 6 1.5 3.5A3.5 3.5 0 0 1 5 0z" fill="#fff"/></svg></span>
        <span class="footer__icon"><svg width="7" height="7" viewBox="0 0 10 10"><path d="M2 0l2 2.5-1 1.2a6 6 0 0 0 3.3 3.3l1.2-1L10 8l-1.5 2C4 10 0 6 0 1.5z" fill="#fff"/></svg></span>
        <span class="footer__icon"><svg width="7" height="7" viewBox="0 0 10 10"><rect x="0.5" y="2" width="9" height="6" fill="none" stroke="#fff"/><path d="M0.5 2L5 5.5 9.5 2" fill="none" stroke="#fff"/></svg></span>
        <span class="footer__icon"><svg width="7" height="7" viewBox="0 0 10 10"><circle cx="5" cy="5" r="4.3" fill="none" stroke="#fff"/><path d="M0.7 5h8.6M5 0.7c-2.4 2.4-2.4 6.2 0 8.6M5 0.7c2.4 2.4 2.4 6.2 0 8.6" fill="none" stroke="#fff" stroke-width="0.8"/></svg></span>
        <span class="footer__rule"></span>
      </div>
      <p class="footer__address">415 Bramwell Avenue #600 Dallas, TX 75219</p>
      <p class="footer__contacts">
        <span>866-402-ACRE</span><span class="footer__sep"></span>
        <span>info@quillridgeacres.example</span><span class="footer__sep"></span>
        <span>www.quillridgeacres.example</span>
      </p>
    </footer>
  </main>
</body>
</html>
```